Business Card Design

Very plain simple card, Plain modern font. Background. Grey fading to black. Large Bright lime green text. Saying.

TWR-ZA.COM

Small other details in white text.

Irish Horse Sales . Livery . Stud . Shows

Mark Dabrowski
TWR
Birch Lodge
Carrowmede Lane
Thistlecombe
Lincolnshire
LN4 7JX

Email. Twrzap@mailvale.co.uk
Tel. 07482 936504

Industry/Entity Type

Business

Contact Information for Business Card

As below

```html
<!DOCTYPE html>
<html lang="en">
<head>
<meta charset="utf-8">
<title>TWR-ZA.COM Business Card</title>
<link rel="stylesheet" href="https://fonts.googleapis.com/css2?family=Source+Sans+3:wght@400;700&display=swap">
<style>
  :root {
    --page-bg: #d9d9d9;
    --card-top: #6f6c6c;
    --card-mid: #262525;
    --card-bottom: #000000;
    --lime: #a6d12c;
    --text-white: #ffffff;
  }
  html, body {
    margin: 0;
    padding: 0;
    width: 1200px;
    height: 1000px;
    overflow: hidden;
    background: var(--page-bg);
  }
  .stage {
    width: 1200px;
    height: 1000px;
    display: flex;
    align-items: center;
    justify-content: center;
  }
  .business-card {
    width: 900px;
    height: 514px;
    box-sizing: border-box;
    background: linear-gradient(to bottom, var(--card-top) 0%, var(--card-mid) 45%, var(--card-bottom) 100%);
    color: var(--text-white);
    font-family: "Source Sans 3", sans-serif;
    text-align: center;
    padding-top: 78px;
  }
  .brand-name {
    margin: 0;
    font-family: "Source Sans 3", sans-serif;
    font-weight: 700;
    font-size: 108px;
    line-height: 1;
    letter-spacing: 2px;
    color: var(--lime);
  }
  .services {
    margin: 14px 0 0;
    font-size: 27px;
    font-weight: 400;
    letter-spacing: 0.3px;
  }
  .services .sep {
    font-size: 16px;
    vertical-align: middle;
    margin: 0 8px;
  }
  .contact {
    margin: 62px 0 0;
    font-style: normal;
    font-size: 24px;
    line-height: 1.3;
  }
  .contact p { margin: 0; }
</style>
</head>
<body>
  <main class="stage">
    <article class="business-card">
      <h1 class="brand-name">TWR-ZA.COM</h1>
      <p class="services">Irish Horse Sales<span class="sep">•</span>Livery<span class="sep">•</span>Stud<span class="sep">•</span>Shows</p>
      <address class="contact">
        <p class="contact-name">Mark Dabrowski</p>
        <p class="contact-address">TWR, Birch Lodge, Carrowmede Lane</p>
        <p class="contact-address">Thistlecombe, Lincolnshire, LN4 7JX</p>
        <p class="contact-email">Email: Twrzap@mailvale.co.uk</p>
        <p class="contact-phone">Tel: 07482 936504</p>
      </address>
    </article>
  </main>
</body>
</html>
```